Silken Roam (A luxury Travel Website)

website text attached in document below

images also attached

feel free to use other images if needed

Target Market(s)

Luxury Seekers and wealthy couples / families

Industry/Entity Type

Luxury Travel

Coding

Coded - Design and coding required

Number of Pages Required

1 page

Requirements
Must have
• A luxury design and easy use.
Nice to have
• Ease of use of page, incorporation of images into the flow of the site

```html
<!DOCTYPE html>
<html lang="en">
<head>
<meta charset="utf-8">
<title>Silken Roam — Luxury Travel</title>
<link href="https://fonts.googleapis.com/css2?family=Cinzel:wght@400;500;600&family=Montserrat:wght@400;500;600&display=swap" rel="stylesheet">
<style>
:root{
  --ink:#000;
  --text:#333;
  --muted:#555;
  --blue:#6db6ea;
  --blue-deep:#3f9ee0;
  --band:#acd5f2;
  --white:#fff;
  --footer:#222;
  --star:#f4c430;
}
*{box-sizing:border-box;margin:0;padding:0}
html,body{width:1200px;height:3996px;overflow:hidden}
body{position:relative;font-family:'Montserrat',sans-serif;color:var(--text);background:var(--white)}
.abs{position:absolute}
.serif{font-family:'Cinzel',serif}

/* header */
.site-header{position:absolute;left:0;top:0;width:1200px;height:75px;background:var(--ink)}
.brand{position:absolute;left:110px;top:20px;font-family:'Montserrat',sans-serif;font-weight:500;font-size:26px;color:var(--white);letter-spacing:.5px}
.brand-dot{display:inline-block;width:10px;height:10px;background:var(--blue);border-radius:50%;margin-right:8px;vertical-align:middle}
.nav a{position:absolute;top:28px;font-size:16px;color:var(--white);text-decoration:none}
.nav a.active{color:var(--blue)}
.btn-start{position:absolute;left:952px;top:17px;width:136px;height:42px;border-radius:21px;background:var(--blue);color:var(--white);font-weight:600;font-size:15px;line-height:42px;text-align:center}

/* hero */
.hero{position:absolute;left:0;top:75px;width:1200px;height:607px;background:linear-gradient(180deg,#233a5e 0%,#3c5477 35%,#6b5640 62%,#1e4a6e 82%,#10304e 100%)}
.hero h1{position:absolute;left:619px;top:148px;width:520px;font-family:'Cinzel',serif;font-weight:500;font-size:34px;line-height:43px;color:var(--white)}
.hero p{position:absolute;left:619px;top:292px;width:470px;font-size:18px;line-height:29px;color:var(--white)}
.btn-book{position:absolute;left:620px;top:382px;width:181px;height:44px;border-radius:22px;background:var(--blue);color:var(--white);font-weight:600;font-size:16px;line-height:44px;text-align:center}
.hero .arrow{position:absolute;top:296px;width:22px;height:22px}

/* band */
.quote-band{position:absolute;left:0;top:682px;width:1200px;height:385px;background:var(--band);text-align:center}
.quote-band .lead{position:absolute;left:0;width:1200px;top:80px;font-size:19px;color:#222}
.btn-shot{position:absolute;left:497px;top:132px;width:206px;height:42px;border-radius:21px;background:var(--ink);color:var(--white);font-weight:600;font-size:16px;line-height:42px}
.quote-band .sub{position:absolute;left:0;width:1200px;top:201px;font-size:19px;color:#222}
.input-box{position:absolute;left:346px;top:259px;width:506px;height:52px;border-radius:26px;background:var(--white);text-align:left}
.input-box span{position:absolute;left:32px;top:16px;font-size:16px;color:#555}
.btn-submit{position:absolute;right:5px;top:5px;width:100px;height:42px;border-radius:21px;background:var(--ink);color:var(--white);font-weight:600;font-size:16px;line-height:42px;text-align:center}

/* headings */
.section-title{position:absolute;left:0;width:1200px;text-align:center;font-family:'Cinzel',serif;font-weight:500;font-size:44px;color:var(--blue)}

/* about */
.about-frame{position:absolute;left:121px;top:1144px;width:361px;height:293px;border:2px solid var(--blue)}
.about-photo{position:absolute;left:112px;top:1152px;width:361px;height:293px;background:linear-gradient(180deg,#3a5fa8 0%,#6f86c2 40%,#c9a9b8 60%,#365984 75%,#14243f 100%);box-shadow:0 4px 12px rgba(0,0,0,.25)}
.about-title{position:absolute;left:561px;top:1178px;font-family:'Cinzel',serif;font-weight:500;font-size:44px;color:var(--blue)}
.about-copy{position:absolute;left:558px;top:1250px;width:531px;font-size:18px;line-height:30px;color:#444;text-align:justify}
.learn{position:absolute;left:560px;top:1392px;font-size:16px;color:var(--blue);font-weight:500}
.learn svg{vertical-align:middle;margin-right:12px}

/* stay cards */
.stay-card{position:absolute;top:1677px;width:298px;height:389px;background:var(--white);box-shadow:0 2px 12px rgba(0,0,0,.12)}
.stay-card .photo{height:181px}
.stay-card h3{position:absolute;left:24px;top:206px;font-family:'Cinzel',serif;font-weight:600;font-size:17px;color:#222}
.stay-card p{position:absolute;left:24px;top:237px;width:260px;font-size:15px;line-height:28px;color:#444}
.stay-card .stars{position:absolute;left:24px;top:344px}
.stay-card .price{position:absolute;right:20px;top:334px;font-family:'Cinzel',serif;font-weight:600;font-size:22px;color:var(--blue)}

/* testimonials */
.review{position:absolute;top:2287px;width:466px;height:271px;background:var(--white);box-shadow:0 2px 14px rgba(0,0,0,.12)}
.review .avatar{position:absolute;left:23px;top:29px;width:102px;height:102px;border-radius:50%;background:linear-gradient(160deg,#c9ccd2,#5a6270)}
.review .name{position:absolute;left:148px;top:33px;font-size:18px;font-weight:500;color:#111}
.review .meta{position:absolute;left:148px;top:64px;font-size:10px;color:#666}
.review .meta svg{vertical-align:middle}
.review p{position:absolute;left:148px;top:94px;width:300px;font-size:15.5px;line-height:30px;color:#444}
.review .mark{position:absolute;left:36px;top:150px}

/* gallery */
.gallery-tile{position:absolute}

/* footer */
.site-footer{position:absolute;left:0;top:3628px;width:1200px;height:368px;background:var(--footer);color:var(--white)}
.site-footer h4{position:absolute;top:64px;font-family:'Cinzel',serif;font-weight:500;font-size:22px;color:var(--white)}
.site-footer .item{position:absolute;font-size:16px;color:var(--white)}
.copyright{position:absolute;left:0;width:1200px;top:324px;text-align:center;font-size:16px}
</style>
</head>
<body>

<header class="site-header">
  <div class="brand"><span class="brand-dot"></span>Silken Roam</div>
  <nav class="nav">
    <a class="active" style="left:615px">Home</a>
    <a style="left:690px">About</a>
    <a style="left:767px">Services</a>
    <a style="left:859px">Contact</a>
  </nav>
  <div class="btn-start">Get Started</div>
</header>

<section class="hero" role="img" aria-label="Resort with palm trees and an illuminated infinity pool at dusk">
  <svg class="arrow" style="left:43px" viewBox="0 0 22 22"><circle cx="11" cy="11" r="10" fill="none" stroke="#fff" stroke-width="1.4"/><path d="M13 6l-5 5 5 5" fill="none" stroke="#fff" stroke-width="1.6"/></svg>
  <svg class="arrow" style="left:1131px" viewBox="0 0 22 22"><circle cx="11" cy="11" r="10" fill="none" stroke="#fff" stroke-width="1.4"/><path d="M9 6l5 5-5 5" fill="none" stroke="#fff" stroke-width="1.6"/></svg>
  <h1>Looking to stay at a 5 star hotel or to fly business class anywhere?</h1>
  <p>Share a screenshot of your travel plans and we beat the price, within 24 hrs.</p>
  <div class="btn-book">Book Your Travel</div>
</section>

<section class="quote-band">
  <div class="lead">We work directly with hotels and airlines to get you the best price,always.</div>
  <div class="btn-shot">Add screenshot here</div>
  <div class="sub">Tell us about your next holiday plans. The more details the better.</div>
  <div class="input-box"><span>Type here...</span><div class="btn-submit">Submit</div></div>
</section>

<section class="about">
  <div class="about-frame"></div>
  <div class="about-photo" role="img" aria-label="Overwater villa and palms reflected in a calm lagoon at sunset"></div>
  <h2 class="about-title">About Us</h2>
  <p class="about-copy">Lorem ipsum dolor sit amet, consectetur adipiscing elit, sed do eiusmod tempor incididunt ut labore et dolore magna aliqua. Quis ipsum suspendisse ultrices gravida. Risus commodo viverra maecenas accumsan lacus vel facilisis.</p>
  <div class="learn"><svg width="40" height="14" viewBox="0 0 40 14"><line x1="0" y1="7" x2="26" y2="7" stroke="#6db6ea" stroke-width="2"/><circle cx="32" cy="7" r="5.5" fill="none" stroke="#6db6ea" stroke-width="2"/></svg>Learn More</div>
</section>

<h2 class="section-title" style="top:1570px">Plan Your Stay</h2>

<article class="stay-card" style="left:112px">
  <div class="photo" role="img" aria-label="Open-air resort lounge with ocean view" style="background:linear-gradient(180deg,#5a4128 0%,#8a7a66 45%,#a59a8c 60%,#4a3522 100%)"></div>
  <h3>Lorem Ipsum 01</h3>
  <p>Lorem ipsumi dolot, consectetur adipiscing elit, seiusmod tempor incididunt ut labore.</p>
  <svg class="stars" width="72" height="13" viewBox="0 0 72 13"><g fill="#f4c430"><path id="st" d="M6.5 0l1.9 4.2 4.6.4-3.5 3 1.1 4.5-4.1-2.4-4.1 2.4 1.1-4.5-3.5-3 4.6-.4z"/><use href="#st" x="14.5"/><use href="#st" x="29"/><use href="#st" x="43.5"/><use href="#st" x="58"/></g></svg>
  <div class="price">$1,420</div>
</article>
<article class="stay-card" style="left:451px">
  <div class="photo" role="img" aria-label="Pool cabana beside an infinity pool and blue sea" style="background:linear-gradient(180deg,#2f7bd6 0%,#5fa6e8 45%,#1f5fae 60%,#8fd0e6 100%)"></div>
  <h3>Lorem Ipsum 02</h3>
  <p>Lorem ipsumi dolot, consectetur adipiscing elit, seiusmod tempor incididunt ut labore.</p>
  <svg class="stars" width="72" height="13" viewBox="0 0 72 13"><g fill="#f4c430"><use href="#st"/><use href="#st" x="14.5"/><use href="#st" x="29"/><use href="#st" x="43.5"/><use href="#st" x="58"/></g></svg>
  <div class="price">$1,420</div>
</article>
<article class="stay-card" style="left:791px">
  <div class="photo" role="img" aria-label="Couple relaxing on a terrace overlooking the sea" style="background:linear-gradient(180deg,#6b5a4a 0%,#a7b4bf 35%,#ded7cf 65%,#8c6e52 100%)"></div>
  <h3>Lorem Ipsum 03</h3>
  <p>Lorem ipsumi dolot, consectetur adipiscing elit, seiusmod tempor incididunt ut labore.</p>
  <svg class="stars" width="72" height="13" viewBox="0 0 72 13"><g fill="#f4c430"><use href="#st"/><use href="#st" x="14.5"/><use href="#st" x="29"/><use href="#st" x="43.5"/><use href="#st" x="58"/></g></svg>
  <div class="price">$1,420</div>
</article>

<h2 class="section-title" style="top:2161px">Customer Testimonials</h2>

<article class="review" style="left:112px">
  <div class="avatar" role="img" aria-label="Reviewer portrait"></div>
  <div class="name">Clara Venn</div>
  <div class="meta"><svg width="14" height="14"><circle cx="7" cy="7" r="6" fill="#9aa3ad"/></svg> Verified review &nbsp;&nbsp;
    <svg width="82" height="13" viewBox="0 0 72 13" style="vertical-align:middle"><g fill="#f4c430"><use href="#st"/><use href="#st" x="14.5"/><use href="#st" x="29"/><use href="#st" x="43.5"/><use href="#st" x="58"/></g></svg></div>
  <p>Sed ut perspiciatis unde omnis natus error sit voluptatem am doloremque laudantium, totam rem aperu, eaque ipsa quae ab illo inventore veritatis et quasi architecto beatae vitae.</p>
  <svg class="mark" width="76" height="60" viewBox="0 0 76 60"><g fill="none" stroke="#9ccbee" stroke-width="2.5"><path d="M32 6C14 10 4 24 6 40c1 10 8 16 16 16s14-6 14-13-6-12-13-12c-3 0-6 1-8 3 2-12 8-20 18-24z"/><path d="M70 6C52 10 42 24 44 40c1 10 8 16 16 16s14-6 14-13-6-12-13-12c-3 0-6 1-8 3 2-12 8-20 18-24z"/></g></svg>
</article>
<article class="review" style="left:622px">
  <div class="avatar" role="img" aria-label="Reviewer portrait" style="background:linear-gradient(160deg,#3a3a3a,#1a1a1a)"></div>
  <div class="name">Theo Marlow</div>
  <div class="meta"><svg width="14" height="14"><circle cx="7" cy="7" r="6" fill="#9aa3ad"/></svg> Verified review &nbsp;&nbsp;
    <svg width="82" height="13" viewBox="0 0 72 13" style="vertical-align:middle"><g fill="#f4c430"><use href="#st"/><use href="#st" x="14.5"/><use href="#st" x="29"/><use href="#st" x="43.5"/><use href="#st" x="58"/></g></svg></div>
  <p>Sed ut perspiciatis unde omnis natus error sit voluptatem am doloremque laudantium, totam rem aperu, eaque ipsa quae ab illo inventore veritatis et quasi architecto beatae vitae.</p>
  <svg class="mark" width="76" height="60" viewBox="0 0 76 60"><g fill="none" stroke="#9ccbee" stroke-width="2.5"><path d="M32 6C14 10 4 24 6 40c1 10 8 16 16 16s14-6 14-13-6-12-13-12c-3 0-6 1-8 3 2-12 8-20 18-24z"/><path d="M70 6C52 10 42 24 44 40c1 10 8 16 16 16s14-6 14-13-6-12-13-12c-3 0-6 1-8 3 2-12 8-20 18-24z"/></g></svg>
</article>

<h2 class="section-title" style="top:2675px">Luxury Living</h2>

<div class="gallery-tile" role="img" aria-label="Traveller relaxing in a business class seat" style="left:112px;top:2952px;width:268px;height:324px;background:linear-gradient(180deg,#d9c9b4 0%,#a88e74 45%,#5a2a2e 75%,#3a1a1e 100%)"></div>
<div class="gallery-tile" role="img" aria-label="Tropical beach breakfast table with fresh juices" style="left:398px;top:2800px;width:267px;height:324px;background:linear-gradient(180deg,#3d5a3a 0%,#9cc6d4 30%,#c58a4e 60%,#8a6236 100%)"></div>
<div class="gallery-tile" role="img" aria-label="Bright bedroom with white bed and botanical wall" style="left:398px;top:3143px;width:267px;height:324px;background:linear-gradient(180deg,#d8d4d2 0%,#a4aaa0 30%,#8d958a 55%,#ecebee 80%,#c9c7cc 100%)"></div>
<div class="gallery-tile" role="img" aria-label="Deck day bed overlooking the sea at dusk" style="left:681px;top:2856px;width:266px;height:324px;background:linear-gradient(180deg,#9a92c0 0%,#c9b4c8 35%,#5e6f9a 60%,#2a3550 100%)"></div>
<div class="gallery-tile" role="img" aria-label="Villa bedroom with carved wooden details and warm lamps" style="left:681px;top:3194px;width:406px;height:324px;background:linear-gradient(180deg,#3a2a1e 0%,#7a4a2a 40%,#a87a50 65%,#4a3020 100%)"></div>

<footer class="site-footer">
  <h4 style="left:113px">Contact</h4>
  <svg class="abs" style="left:113px;top:110px" width="16" height="20" viewBox="0 0 16 20"><path d="M8 1C4 1 1.5 4 1.5 7.5 1.5 12 8 19 8 19s6.5-7 6.5-11.5C14.5 4 12 1 8 1z" fill="none" stroke="#fff" stroke-width="1.6"/><circle cx="8" cy="7.5" r="2.4" fill="none" stroke="#fff" stroke-width="1.6"/></svg>
  <div class="item" style="left:144px;top:112px">Silken Roam,</div>
  <div class="item" style="left:144px;top:141px">Address Comes here</div>
  <svg class="abs" style="left:113px;top:193px" width="16" height="12" viewBox="0 0 16 12"><rect x="0" y="0" width="16" height="12" rx="1.5" fill="#fff"/><path d="M1 1l7 6 7-6" fill="none" stroke="#222" stroke-width="1.4"/></svg>
  <div class="item" style="left:144px;top:188px">hello@silkenroam.com</div>
  <svg class="abs" style="left:113px;top:240px" width="14" height="14" viewBox="0 0 24 24"><path d="M6.6 10.8a15.1 15.1 0 006.6 6.6l2.2-2.2c.3-.3.7-.4 1-.2 1.1.4 2.3.6 3.6.6.6 0 1 .4 1 1V20c0 .6-.4 1-1 1A17 17 0 013 4c0-.6.4-1 1-1h3.5c.6 0 1 .4 1 1 0 1.3.2 2.5.6 3.6.1.3 0 .7-.2 1z" fill="#fff"/></svg>
  <div class="item" style="left:144px;top:236px">T. +1 555-014-2290</div>

  <h4 style="left:448px">Quick Links</h4>
  <div class="item" style="left:449px;top:112px">Home</div>
  <div class="item" style="left:449px;top:141px">About</div>
  <div class="item" style="left:449px;top:171px">Our Hotels</div>
  <div class="item" style="left:449px;top:201px">Testimonials</div>
  <div class="item" style="left:449px;top:231px">Contact</div>

  <h4 style="left:705px">Other Links</h4>
  <div class="item" style="left:706px;top:112px">Terms &amp; Conditions</div>
  <div class="item" style="left:706px;top:141px">Privacy &nbsp;Policy</div>
  <div class="item" style="left:706px;top:171px">FAQs</div>

  <h4 style="left:970px">Follow Us</h4>
  <svg class="abs" style="left:970px;top:111px" width="14" height="14"><circle cx="7" cy="7" r="6" fill="#fff"/></svg>
  <div class="item" style="left:1001px;top:108px">Community</div>
  <svg class="abs" style="left:973px;top:152px" width="14" height="14"><rect x="1" y="1" width="12" height="12" rx="2" fill="none" stroke="#fff" stroke-width="1.6"/></svg>
  <div class="item" style="left:1001px;top:150px">Photo Journal</div>

  <div class="copyright">2022 Silken Roam. All Rights Reserved.</div>
</footer>

</body>
</html>
```